web Design for Architecture and Interior Design Firm

This is a complete redesign of an architecture and interior design firm.( http://www.kelbrixa.com )
We have established a new look-n-feel for them and need to apply it to the new site/new architecture. Wireframes attached with logo and PDF of new brochure.
This will require a quck turn-around. The client is expecting a very modern design with web 2.0 in mind.
Again very quick turn-around! If you cannot commit to a Friday deliverable, do not bid! Must be completed by no later than Friday!

```html
<!DOCTYPE html>
<html lang="en">
<head>
<meta charset="utf-8">
<title>Kelbrixa Design Studios</title>
<link rel="stylesheet" href="https://fonts.googleapis.com/css2?family=Jost:wght@400;500&family=Arimo:wght@400;700&display=swap">
<style>
  :root {
    --brand-red: #c8102e;
    --page-red: #c81432;
    --paper: #ffffff;
    --ink: #3a3a3a;
    --heading: #5b5247;
    --nav: #333333;
    --rule: #bdbdbd;
    --caption-bg: rgba(70, 70, 70, 0.62);
  }
  * { margin: 0; padding: 0; box-sizing: border-box; }
  html, body { width: 1200px; height: 1031px; overflow: hidden; }
  body {
    position: relative;
    background: var(--page-red);
    font-family: "Arimo", Arial, sans-serif;
    color: var(--ink);
  }
  .page-backdrop {
    position: absolute; inset: 0;
    background: linear-gradient(90deg, #c41230 0%, #cc1a36 50%, #c41230 100%);
  }
  .sheet {
    position: absolute; left: 159px; top: 0; width: 882px; height: 947px;
    background: var(--paper);
  }
  .brand {
    position: absolute; left: 61px; top: 26px;
    font-family: "Jost", sans-serif; font-weight: 500;
    font-size: 33px; letter-spacing: 0.5px;
    color: var(--brand-red);
  }
  .main-nav {
    position: absolute; left: 404px; top: 64px;
    display: flex; font-family: "Jost", sans-serif; font-size: 13px;
    color: var(--nav); text-transform: uppercase;
  }
  .main-nav a { color: inherit; text-decoration: none; }
  .main-nav a.is-current { color: var(--brand-red); }
  .main-nav .sep { margin: 0 10px; color: #888; }
  .hero {
    position: absolute; left: 28px; top: 114px; width: 825px; height: 422px;
    background: linear-gradient(100deg, #d9d6d0 0%, #8a8680 28%, #3a2a20 45%, #b86a2a 60%, #2e2a26 85%, #6a6660 100%);
  }
  .hero-caption {
    position: absolute; right: 0; top: 298px; width: 288px; height: 94px;
    background: var(--caption-bg);
    display: flex; align-items: center; justify-content: center;
    font-family: "Jost", sans-serif; font-size: 26px; color: #fff;
  }
  .hero-band {
    position: absolute; left: 28px; top: 536px; width: 825px; height: 10px;
    background: var(--brand-red);
  }
  .intro { position: absolute; left: 42px; top: 565px; width: 520px; }
  .intro h1 {
    font-size: 22px; line-height: 27px; font-weight: 700;
    color: var(--heading); margin-bottom: 19px;
  }
  .intro p { font-size: 10.6px; line-height: 16.2px; margin-bottom: 16px; }
  .sidebar { position: absolute; left: 611px; top: 568px; width: 240px; }
  .sidebar h2 {
    font-family: "Jost", sans-serif; font-weight: 400; font-size: 14.5px;
    color: var(--heading); text-transform: uppercase;
  }
  .news-list { margin-top: 16px; }
  .news-item { margin-bottom: 11px; font-size: 10px; line-height: 12px; width: 225px; }
  .news-item h3 { font-size: 10px; font-weight: 400; color: var(--brand-red); }
  .news-item a { color: #222; text-decoration: underline; }
  .newsletter { margin-top: 23px; }
  .field { display: flex; align-items: center; margin-top: 14px; font-size: 10px; }
  .field:first-of-type { margin-top: 15px; }
  .field label { width: 42px; }
  .field input { width: 152px; height: 18px; border: 1px solid #8c8c8c; }
  .actions { display: flex; gap: 12px; margin: 16px 0 0 42px; }
  .actions button {
    width: 71px; height: 22px; font-family: inherit; font-size: 10px; color: #222;
    border: 1px solid #999; border-radius: 3px;
    background: linear-gradient(#f4f4f4, #c8c8c8);
  }
  .footer-rule {
    position: absolute; left: 28px; top: 894px; width: 825px; height: 1px;
    background: var(--rule);
  }
  .footer {
    position: absolute; left: 28px; top: 909px; width: 825px;
    display: flex; justify-content: space-between; align-items: center;
    font-size: 9.5px; color: #444;
  }
  .follow { display: flex; align-items: center; gap: 5px; }
  .follow span { margin-right: 4px; }
  .social-square { width: 10px; height: 10px; background: #333; }
</style>
</head>
<body>
  <div class="page-backdrop" role="img" aria-label="Red background with faint architectural floor plan drawings"></div>
  <div class="sheet">
    <div class="brand">KELBRIXA</div>
    <nav class="main-nav">
      <a class="is-current" href="#">Home</a><span class="sep">|</span>
      <a href="#">About Us</a><span class="sep">|</span>
      <a href="#">Services</a><span class="sep">|</span>
      <a href="#">Portfolio</a><span class="sep">|</span>
      <a href="#">Career</a><span class="sep">|</span>
      <a href="#">Contact Us</a>
    </nav>

    <div class="hero" role="img" aria-label="Meeting room with orange chairs, white table and a wall of colourful circular panels">
      <div class="hero-caption">Norvane Media Office</div>
    </div>
    <div class="hero-band"></div>

    <section class="intro">
      <h1>Kelbrixa Design Studios Makes the<br>Process Predictable</h1>
      <p>When something as important as the very space in which your business lives and works is about to be disrupted, you should be confident you've chosen the right space and the best team to ensure a successful project. Rely on Kelbrixa Design Studios to meet your needs and to make the process predictable. You can be assured that your project goals and objectives will be achieved.</p>
      <p>Rely on Kelbrixa Design Studios to meet your needs and to make the process predictable. You can be assured that your project goals and objectives will be achieved. When something as important as the very space in which your business lives and works is about to be disrupted, you should be confident you've chosen the right space and the best team to ensure a successful project.</p>
    </section>

    <aside class="sidebar">
      <h2>News</h2>
      <div class="news-list">
        <article class="news-item">
          <h3>News Title 1</h3>
          <p>Lorem ipsum dolor sit amet, consectetur adipisc-ing elit. Mauris vitae dui nunc. Nullam lacus lacus...<a href="#">more</a></p>
        </article>
        <article class="news-item">
          <h3>New Office Location</h3>
          <p>Lorem ipsum dolor sit amet, consectetur adipisc-ing elit. Mauris vitae dui nunc. Nullam lacus lacus...<a href="#">more</a></p>
        </article>
      </div>
      <form class="newsletter">
        <h2>Newsletter</h2>
        <div class="field"><label for="nl-name">Name</label><input id="nl-name" type="text"></div>
        <div class="field"><label for="nl-email">Email</label><input id="nl-email" type="text"></div>
        <div class="actions">
          <button type="button">Subscribe</button>
          <button type="button">Unsubscribe</button>
        </div>
      </form>
    </aside>

    <div class="footer-rule"></div>
    <footer class="footer">
      <span>© 2011 Kelbrixa Design Studios.</span>
      <div class="follow">
        <span>Follow us</span>
        <div class="social-square" aria-label="Social link"></div>
        <div class="social-square" aria-label="Social link"></div>
      </div>
    </footer>
  </div>
</body>
</html>
```